GUARANTEED WordPress design needed for a sassy, confident charisma coach!

We need a website design for Marla Penrick's brand new, responsive, Wordpress website.
Marla is a trainer / coach who teaches people how to be more charismatic and runs events, publishes video courses and has an ongoing video blog. Her old website is here: www.marlapenrick.co.uk ... but it's now time to have a much better site!
We have a strong idea about the technical components of the website, but we need a designer's eye to create a great style for the site (and provide layered PSD files which our developers will then convert to HTML and CSS).
Marla's brand is sassy, brave, warm and confident. The videos on her existing site give quite a good feel for her personality. We need a clean, stylish and compelling page that isn't too corporate and captures her personality. Every element needs to feel coherent, from fonts and headings to colours and spacing.
The following sites are not exactly what Marla wants (and certainly aren't right in terms of colours) but they give you an idea of the kind of people she is competing against and the area she is operating in:
http://www.tessa-broughley.example/
http://rowanfelsby.example/
Ideally, you will have done something similar and be able to key in on exactly the kind of thing we want: we're not looking to reinvent the wheel. Hopefully you won't mind tweaking a few things if you are close to what we need.
More detail is provided in the word document attached. But in a nutshell we need: a banner, footer, sign-up strap, menu bar, signature and 4 different basic page types. We want bursts of bright colours, contrasted with black and white if possible - sorry we can't be more specific than that...
The word doc also contains some amateur mock-ups as well (the images are also just mockups at this stage) - but although these give a general sense of the structure what we are looking for, we are clearly not designers...so please help! We need a designer's touch!
Kind regards,
Corin
PS The layered PSD versions of the mockup files are available on Cloudvantre: https://files.cloudvantre.example/sh/k72pqa4w1zbtmrd/QXvenlr8Ty3PwMiU6Hs2kYfDb?dl=0
Target Market(s)
Entrepreneurs who need to sell themselves.
Number of Pages Required
4 page

```html
<!DOCTYPE html>
<html lang="en">
<head>
<meta charset="utf-8">
<title>Marla Penrick — The Image and Impact Specialist</title>
<link rel="stylesheet" href="https://fonts.googleapis.com/css2?family=Oswald:wght@400;500&family=Open+Sans:wght@400;600&display=swap">
<style>
:root{
  --red:#8b1a2b;
  --red-bright:#c8303a;
  --ink:#222;
  --text:#555;
  --muted:#999;
  --line:#e3e3e3;
  --panel:#f2f2f2;
  --cream:#f8eaa7;
  --gold:#e6c23a;
  --hero:#2a2a2a;
  --grey-tag:#9a9fa6;
  --icon:#8a8a8a;
  --follow-1:#3b5998;
  --follow-2:#4aa3df;
  --follow-3:#d34836;
  --follow-4:#c4302b;
}
*{box-sizing:border-box;margin:0;padding:0}
html,body{width:1200px;height:3309px;overflow:hidden;background:#fff}
body{position:relative;font-family:'Open Sans',Arial,sans-serif;color:var(--text)}
.abs{position:absolute}

/* header */
.social-top{left:82px;top:57px;display:flex;gap:13px;align-items:center}
.social-top span{width:10px;height:10px;border-radius:2px;background:var(--icon)}
.brand{left:0;width:1200px;top:34px;text-align:center}
.brand-name{font-family:'Oswald',Arial,sans-serif;font-size:40px;font-weight:500;color:var(--ink);line-height:48px;letter-spacing:1px}
.brand-tag{font-size:13px;color:var(--red-bright);margin-top:2px}
.search{left:907px;top:44px;width:214px;height:36px;border:1px solid #ccc;border-radius:18px;font-size:11px;color:#999;padding:10px 18px}
.search svg{position:absolute;right:14px;top:10px}
.rule{left:79px;width:1042px;height:1px;background:var(--line)}
.nav{left:79px;width:1042px;top:143px;display:flex;justify-content:space-around;font-family:'Oswald',Arial,sans-serif;font-size:14px;color:#888;letter-spacing:.5px}

/* hero */
.hero{left:0;top:187px;width:1200px;height:453px;background:var(--hero)}
.hero-photo{right:0;top:0;width:460px;height:453px;background:linear-gradient(90deg,#2a2a2a 0%,#7a5a4e 35%,#c88f78 60%,#b8242c 100%)}
.hero-title{left:141px;top:72px;font-family:'Oswald',Arial,sans-serif;font-size:44px;line-height:52px;color:#fff;font-weight:500}
.hero-bar{left:141px;top:243px;width:245px;height:4px;background:var(--gold)}
.hero-copy{left:141px;top:262px;font-size:13px;line-height:26px;color:#fff}
.btn{display:inline-block;background:var(--red);color:#fff;font-size:12px;font-weight:600;text-align:center}
.hero-btn{left:141px;top:323px;width:135px;height:39px;line-height:39px;border-radius:20px}

/* newsletter strap */
.strap{left:0;top:642px;width:1200px;height:66px;background:var(--cream);border-top:2px solid #ead68a;border-bottom:2px solid #ead68a}
.strap-title{left:97px;top:12px;font-family:'Oswald',Arial,sans-serif;font-size:14px;line-height:18px;color:var(--ink)}
.strap-input{top:16px;height:33px;background:#fff;font-size:9px;color:#aaa;padding:11px 18px;letter-spacing:.5px}
.strap-btn{left:909px;top:16px;width:192px;height:33px;line-height:33px;font-size:9px;letter-spacing:1px;background:var(--red);color:#fff;text-align:center;font-weight:600}

/* posts */
.post{left:79px;width:684px;background:#fff;box-shadow:0 2px 4px rgba(0,0,0,.06);text-align:center}
.post-media{width:684px;position:relative}
.media-badge{position:absolute;left:330px;bottom:-8px;width:24px;height:18px;background:#fff;border:1px solid #bbb}
.post-cat{margin-top:42px;font-size:10px;letter-spacing:1px;color:var(--muted)}
.post-title{font-family:'Oswald',Arial,sans-serif;font-size:20px;font-weight:500;color:var(--ink);margin-top:8px;letter-spacing:.5px}
.post-meta{font-size:10px;color:var(--muted);margin-top:6px;letter-spacing:.5px}
.post-meta span{margin:0 18px}
.post-body{width:614px;margin:14px auto 0;font-size:11.5px;line-height:21.6px;color:#555}
.read-more{display:inline-block;margin-top:8px;font-size:8px;letter-spacing:1.5px;color:#555;border-bottom:1px solid #ccc;padding:2px 10px}
.post-foot{margin:26px 44px 0;border-top:1px solid var(--line);height:58px;display:flex;justify-content:space-between;align-items:center;font-size:9px;color:var(--muted);letter-spacing:1px}
.post-foot .share{display:flex;gap:22px}
.post-foot .share span{width:9px;height:9px;border-radius:2px;background:#777}

/* sidebar */
.widget{left:792px;width:329px}
.subscribe{top:746px;height:286px;background:var(--panel);text-align:center;padding-top:22px}
.widget-title{font-family:'Oswald',Arial,sans-serif;font-size:20px;font-weight:500;color:var(--ink)}
.subscribe p{font-size:13px;line-height:26px;color:#777;margin:22px 24px 0}
.subscribe .field{margin:18px 18px 0;height:45px;background:#fff;font-size:12px;font-style:italic;color:#aaa;line-height:45px}
.subscribe .btn{margin-top:16px;width:176px;height:44px;line-height:44px;border-radius:22px}
.popular{top:1074px;height:382px;background:var(--panel);padding:16px 16px 0}
.tabs{display:flex;justify-content:space-between;align-items:center;font-family:'Oswald',Arial,sans-serif;font-size:13px;color:var(--ink)}
.tabs .active{background:var(--red);color:#fff;width:144px;height:44px;line-height:44px;border-radius:22px;text-align:center}
.pop-item{display:flex;gap:14px;padding:16px 0;border-bottom:1px solid #ddd}
.pop-item:last-child{border-bottom:0}
.thumb{width:79px;height:79px;flex:none}
.pop-item h4{font-family:'Oswald',Arial,sans-serif;font-weight:400;font-size:13px;color:var(--ink)}
.pop-item .date{font-size:10px;color:#999;margin-top:4px}
.pop-item p{font-size:10px;line-height:15px;color:#888;margin-top:4px}
.side-head{font-family:'Oswald',Arial,sans-serif;font-size:13px;color:var(--ink);padding-bottom:10px;border-bottom:2px solid var(--line)}
.follow-row{display:flex;align-items:center;gap:14px;height:46px;font-size:12px;color:#888}
.follow-row i{width:42px;height:42px;display:block}
.tag-row{display:flex;align-items:center;height:40px;margin-bottom:5px;font-family:'Oswald',Arial,sans-serif;font-size:13px;color:#666}
.tag-row .arrow{width:38px;height:40px;background:var(--grey-tag);display:flex;align-items:center;justify-content:center}
.tag-row .label{flex:1;padding-left:14px}
.tag-row .count{width:44px;height:40px;line-height:40px;text-align:center;background:var(--grey-tag);color:#fff}
.tag-row.on .arrow,.tag-row.on .count{background:var(--red)}
.tag-row.on .label{color:var(--ink)}

/* promo */
.promo{left:792px;top:2146px;width:329px;height:700px;background:linear-gradient(180deg,#5d5047 0%,#3f3a37 45%,#4b4540 100%);overflow:hidden}
.promo-title{left:10px;top:6px;font-family:'Oswald',Arial,sans-serif;font-size:40px;line-height:44px;color:rgba(255,255,255,.85);font-weight:500}
.promo-live{left:0;width:329px;top:320px;text-align:center;font-family:'Oswald',Arial,sans-serif;font-size:76px;color:#fff;font-weight:500}
.promo-note{left:0;width:329px;top:460px;text-align:center;font-size:30px;line-height:42px;color:#fff;font-style:italic}
.promo-btn{left:61px;top:572px;width:207px;height:66px;line-height:66px;border-radius:33px;font-size:19px}
.promo-bar{left:0;bottom:0;width:329px;height:35px;background:rgba(40,40,40,.85);font-size:12px;color:#fff;display:flex;align-items:center;padding:0 10px;gap:6px}
.promo-bar i{width:22px;height:22px;background:#555;display:flex;align-items:center;justify-content:center}
.promo-bar span{margin-left:auto}

/* footer */
.to-top{left:574px;top:3088px;width:55px;height:62px;background:var(--red);z-index:2;display:flex;align-items:center;justify-content:center}
.footer{left:22px;top:3115px;width:1156px;height:194px;background:#f5f5f5}
.footer-nav{left:180px;width:796px;top:78px;display:flex;justify-content:space-between;font-family:'Oswald',Arial,sans-serif;font-size:12px;color:#888;letter-spacing:.5px}
.footer-rule{left:180px;width:796px;top:132px;height:1px;background:#e2e2e2}
.copyright{left:0;width:1156px;top:158px;text-align:center;font-size:11px;color:#bbb}
</style>
</head>
<body>

<header>
  <div class="abs social-top"><span></span><span></span><span></span><span></span><span></span><span></span></div>
  <div class="abs brand">
    <div class="brand-name">Marla Penrick</div>
    <div class="brand-tag">The Image and Impact Specialist</div>
  </div>
  <div class="abs search">Enter your search term
    <svg width="14" height="14" viewBox="0 0 14 14"><circle cx="6" cy="6" r="4.5" fill="none" stroke="#555" stroke-width="1.6"/><line x1="9.3" y1="9.3" x2="13" y2="13" stroke="#555" stroke-width="1.6"/></svg>
  </div>
  <div class="abs rule" style="top:119px"></div>
  <nav class="abs nav"><span>HOME</span><span>EVENT</span><span>WORK WITH ME</span><span>CORPORATE</span><span>ABOUT</span><span>CONTACT</span></nav>
  <div class="abs rule" style="top:185px"></div>
</header>

<section class="abs hero">
  <div class="abs hero-photo" role="img" aria-label="Portrait of Marla smiling in a red jacket"></div>
  <h1 class="abs hero-title">ATTRACT<br>CONNECT<br>INFLUENCE</h1>
  <div class="abs hero-bar"></div>
  <p class="abs hero-copy">Lorem Ipsum is simply dummy text of the printing and typesetting industry.<br>Lorem Ipsum has been the industry's standard dummy text ever since the 1500s.</p>
  <a class="abs btn hero-btn">Read More</a>
</section>

<section class="abs strap">
  <div class="abs strap-title">SIGNUP TO<br>NEWSLETTER</div>
  <div class="abs strap-input" style="left:254px;width:306px">YOUR NAME</div>
  <div class="abs strap-input" style="left:582px;width:305px">YOUR EMAIL ADDRESS</div>
  <div class="abs strap-btn">SUBSCRIBE NOW</div>
</section>

<article class="abs post" style="top:746px">
  <div class="post-media" style="height:331px;background:radial-gradient(circle at 40% 50%,#f08a70,#e2553e 70%)" role="img" aria-label="Marla speaking on stage against a coral backdrop">
    <div style="position:absolute;right:0;top:0;width:30px;height:30px;background:var(--red-bright)"></div>
    <div class="media-badge"></div>
  </div>
  <div class="post-cat">MOTIVATION</div>
  <h2 class="post-title">PUBLIC SPEAKING...MADE EASY</h2>
  <div class="post-meta"><span>MARLA PENRICK'S</span><span>18 MAY 2016</span></div>
  <p class="post-body">Lorem ipsum dolor sit amet, consectetur adipisicing elit, sed do eiusmod tempor incididunt ut labore et dolore magna aliqua. Ut enim ad minim veniam, quis nostrud exercitation ullamco laboris nisi ut aliquip ex ea commodo consequat. Duis aute irure dolor in reprehenderit in voluptate velit esse cillum dolore eigiat nulla pariatur. Excepteur sint occaecat cupidatat non proident, sunt in culpa qui officia deserunt mollit anim id it laborum. Sed ut perspiciatis unde omnis iste natus error sit voluptatem accusantium doloremque laudantium, totam rem aperiam, eaque ipsa quae ab illo inventore ut labore et dolore now is the great working with travlling magnam aliquam quaerat voluptatem.</p>
  <span class="read-more">READ MORE</span>
  <div class="post-foot"><div>&#9643; 02 COMMENTS &nbsp;&nbsp;&nbsp;&nbsp; &#9825; LIKES 25</div><div class="share"><span></span><span></span><span></span><span></span></div></div>
</article>

<article class="abs post" style="top:1513px">
  <div class="post-media" style="height:378px;background:linear-gradient(90deg,#d8d8d8 0%,#b9b9b9 34%,#8a4b45 34%,#9c5a50 66%,#e2e2e2 66%,#c8c8c8 100%)" role="img" aria-label="Collage of Marla in different outfits and dresses">
    <div class="media-badge"></div>
  </div>
  <div class="post-cat">MOTIVATION</div>
  <h2 class="post-title">PUBLIC SPEAKING...MADE EASY</h2>
  <div class="post-meta"><span>MARLA PENRICK'S</span><span>18 MAY 2016</span></div>
  <p class="post-body">Lorem ipsum dolor sit amet, consectetur adipisicing elit, sed do eiusmod tempor incididunt ut labore et dolore magna aliqua. Ut enim ad minim veniam, quis nostrud exercitation ullamco laboris nisi ut aliquip ex ea commodo consequat. Duis aute irure dolor in reprehenderit in voluptate velit esse cillum dolore eigiat nulla pariatur. Excepteur sint occaecat cupidatat non proident, sunt in culpa qui officia deserunt mollit anim id it laborum. Sed ut perspiciatis unde omnis iste natus error sit voluptatem accusantium doloremque laudantium, totam rem aperiam, eaque ipsa quae ab illo inventore ut labore et dolore now is the great working with travlling magnam aliquam quaerat voluptatem.</p>
  <span class="read-more">READ MORE</span>
  <div class="post-foot"><div>&#9643; 02 COMMENTS &nbsp;&nbsp;&nbsp;&nbsp; &#9825; LIKES 25</div><div class="share"><span></span><span></span><span></span><span></span></div></div>
</article>

<article class="abs post" style="top:2323px">
  <div class="post-media" style="height:331px;background:linear-gradient(90deg,#d9d4cc 0%,#a79886 40%,#6a4a3e 70%,#b8323a 100%)" role="img" aria-label="Video still of Marla talking to camera">
    <div style="position:absolute;right:6px;top:6px;display:flex;flex-direction:column;gap:4px">
      <svg width="24" height="24" viewBox="0 0 24 24"><rect width="24" height="24" fill="#222"/><path d="M12 18l-6-6a3.3 3.3 0 0 1 6-3a3.3 3.3 0 0 1 6 3z" fill="#fff"/></svg>
      <svg width="24" height="24" viewBox="0 0 24 24"><rect width="24" height="24" fill="#222"/><circle cx="12" cy="12" r="6" fill="none" stroke="#fff" stroke-width="1.6"/><path d="M12 8v4h3" stroke="#fff" stroke-width="1.6" fill="none"/></svg>
      <svg width="24" height="24" viewBox="0 0 24 24"><rect width="24" height="24" fill="#222"/><path d="M6 12l12-6-4 13-3-5z" fill="#fff"/></svg>
    </div>
    <div style="position:absolute;left:0;bottom:0;width:684px;height:30px;background:rgba(0,0,0,.75);display:flex;align-items:center;gap:10px;padding:0 10px;font-size:10px;color:#fff">
      <svg width="12" height="12" viewBox="0 0 12 12"><path d="M2 1l9 5-9 5z" fill="#fff"/></svg>
      <span style="background:#333;padding:1px 4px">04:21</span>
      <div style="flex:1;height:6px;background:#444"></div>
      <span style="font-weight:600">HD Vidloom</span>
    </div>
    <div class="media-badge"></div>
  </div>
  <div class="post-cat">MOTIVATION</div>
  <h2 class="post-title">PUBLIC SPEAKING...MADE EASY</h2>
  <div class="post-meta"><span>MARLA PENRICK'S</span><span>18 MAY 2016</span></div>
  <p class="post-body">Lorem ipsum dolor sit amet, consectetur adipisicing elit, sed do eiusmod tempor incididunt ut labore et dolore magna aliqua. Ut enim ad minim veniam, quis nostrud exercitation ullamco laboris nisi ut aliquip ex ea commodo consequat. Duis aute irure dolor in reprehenderit in voluptate velit esse cillum dolore eigiat nulla pariatur. Excepteur sint occaecat cupidatat non proident, sunt in culpa qui officia deserunt mollit anim id it laborum. Sed ut perspiciatis unde omnis iste natus error sit voluptatem accusantium doloremque laudantium, totam rem aperiam, eaque ipsa quae ab illo inventore ut labore et dolore now is the great working with travlling magnam aliquam quaerat voluptatem.</p>
  <span class="read-more">READ MORE</span>
  <div class="post-foot"><div>&#9643; 02 COMMENTS &nbsp;&nbsp;&nbsp;&nbsp; &#9825; LIKES 25</div><div class="share"><span></span><span></span><span></span><span></span></div></div>
</article>

<aside>
  <div class="abs widget subscribe">
    <h3 class="widget-title">SUBSCRIBE NOW</h3>
    <p>Lorem ipsum dolor sit amet, consectetur adipiscing elit.</p>
    <div class="field">Enter your Email</div>
    <a class="btn">SUBSCRIBE NOW</a>
  </div>

  <div class="abs widget popular">
    <div class="tabs"><span>POPULAR POSTS</span><span class="active">LATEST POSTS</span></div>
    <div class="pop-item"><div class="thumb" role="img" aria-label="Black and white portrait thumbnail" style="background:linear-gradient(135deg,#888,#333)"></div><div><h4>Lorem ipsum dolor sit amet.</h4><div class="date">21 DECEMBER 2015</div><p>Lorem ipsum dolor sit amet, consecte-tur adipiscing elit.</p></div></div>
    <div class="pop-item"><div class="thumb" role="img" aria-label="Person working at a desk thumbnail" style="background:linear-gradient(135deg,#aab,#445)"></div><div><h4>Nunc malesuada elementum.</h4><div class="date">21 DECEMBER 2015</div><p>Lorem ipsum dolor sit amet, consecte-tur adipiscing elit.</p></div></div>
    <div class="pop-item"><div class="thumb" role="img" aria-label="Green hillside landscape thumbnail" style="background:linear-gradient(180deg,#cfe0ea,#5d8a4a)"></div><div><h4>Nunc malesuada elementum.</h4><div class="date">21 DECEMBER 2015</div><p>Lorem ipsum dolor sit amet, consecte-tur adipiscing elit.</p></div></div>
  </div>

  <div class="abs widget" style="top:1478px">
    <div class="side-head">FOLLOW ME</div>
    <div style="margin-top:12px">
      <div class="follow-row"><i style="background:var(--follow-1)"></i>1000 Followers</div>
      <div class="follow-row"><i style="background:var(--follow-2)"></i>1400 Followers</div>
      <div class="follow-row"><i style="background:var(--follow-3)"></i>1234 Followers</div>
      <div class="follow-row"><i style="background:var(--follow-4)"></i>4356 Subscribers</div>
    </div>
  </div>

  <div class="abs widget" style="top:1732px">
    <div class="side-head">TAGS</div>
    <div style="margin-top:14px">
      <div class="tag-row"><span class="arrow"><svg width="16" height="10" viewBox="0 0 16 10"><path d="M0 5h14M10 1l4 4-4 4" stroke="#fff" stroke-width="1.5" fill="none"/></svg></span><span class="label">POWER POSE</span><span class="count">10</span></div>
      <div class="tag-row on"><span class="arrow"><svg width="16" height="10" viewBox="0 0 16 10"><path d="M0 5h14M10 1l4 4-4 4" stroke="#fff" stroke-width="1.5" fill="none"/></svg></span><span class="label">CAPSULE WARDROBE</span><span class="count">30</span></div>
      <div class="tag-row"><span class="arrow"><svg width="16" height="10" viewBox="0 0 16 10"><path d="M0 5h14M10 1l4 4-4 4" stroke="#fff" stroke-width="1.5" fill="none"/></svg></span><span class="label">RAPPORT</span><span class="count">12</span></div>
      <div class="tag-row"><span class="arrow"><svg width="16" height="10" viewBox="0 0 16 10"><path d="M0 5h14M10 1l4 4-4 4" stroke="#fff" stroke-width="1.5" fill="none"/></svg></span><span class="label">HANDSHAKE</span><span class="count">23</span></div>
      <div class="tag-row"><span class="arrow"><svg width="16" height="10" viewBox="0 0 16 10"><path d="M0 5h14M10 1l4 4-4 4" stroke="#fff" stroke-width="1.5" fill="none"/></svg></span><span class="label">VISION BOARD</span><span class="count">15</span></div>
      <div class="tag-row"><span class="arrow"><svg width="16" height="10" viewBox="0 0 16 10"><path d="M0 5h14M10 1l4 4-4 4" stroke="#fff" stroke-width="1.5" fill="none"/></svg></span><span class="label">BODY LANGUAGE</span><span class="count">25</span></div>
    </div>
  </div>

  <div class="abs promo" role="img" aria-label="Marla presenting live to an audience in a bright room">
    <div class="abs promo-title">UNLOCK<br>THE<br>SUPERPOWER<br>OF CHARISMA</div>
    <div class="abs promo-live">LIVE</div>
    <div class="abs promo-note">* Only 6<br>places left.</div>
    <a class="abs btn promo-btn">Read More</a>
    <div class="abs promo-bar">
      <i><svg width="8" height="10" viewBox="0 0 8 10"><path d="M6 1L2 5l4 4" stroke="#fff" stroke-width="1.5" fill="none"/></svg></i>
      <i><svg width="8" height="10" viewBox="0 0 8 10"><path d="M2 1l4 4-4 4" stroke="#fff" stroke-width="1.5" fill="none"/></svg></i>
      <span>Lorem ipsum dolor sit amet</span>
    </div>
  </div>
</aside>

<footer>
  <div class="abs to-top"><svg width="16" height="24" viewBox="0 0 16 24"><path d="M8 23V2M2 8l6-6 6 6" stroke="#fff" stroke-width="1.5" fill="none"/></svg></div>
  <div class="abs footer">
    <nav class="abs footer-nav"><span>HOME</span><span>EVENT</span><span>WORK WITH ME</span><span>CORPORATE</span><span>ABOUT</span><span>CONTACT</span></nav>
    <div class="abs footer-rule"></div>
    <div class="abs copyright">2016 Marla Penrick's, All rights reserved.</div>
  </div>
</footer>

</body>
</html>
```